Street Sign Project - Attract Customers

We need a street sign designed to display out the front of the building. It design will need to be 1800mm wide x 900mm high. We need to show potential customers where we are inviting. Some of the attachments are for inspiration. The sign will be printed on a sheet of aluminum. if you have a good look at our web site which is www.pk-r.com.au you should get a good feeling about the company and what we do.

Target Market(s)

Construction companies, landscaping and civil earth moving companies who may drive past our business

Industry/Entity Type

Building

Font styles to use
Sans Serif

Colors
ffffff
3277b5
000000

Requirements
Must have
• Company logo must be the main focus point
• The number "54" on the sign to show street number (300mm high)
• phone number - (02) 9418 3065
• web address - www.pk-r.com.au
• I have loaded pictures i would like to see used in the sign
Nice to have
• Banner picture as attached
Should not have
• Bright colours. Please use our blue colour where possible

```html
<!DOCTYPE html>
<html lang="en">
<head>
<meta charset="utf-8">
<title>Peak &amp; Rise Hoisting – Street Sign</title>
<link rel="stylesheet" href="https://fonts.googleapis.com/css2?family=Archivo+Black&display=swap">
<style>
  :root {
    --brand-blue: #3277b5;
    --brand-blue-bright: #1e8fd6;
    --brand-blue-pale: #dbe9f5;
    --ink: #1a1a1a;
    --paper: #ffffff;
    --photo-border: #d9d9d9;
  }
  * { box-sizing: border-box; margin: 0; padding: 0; }
  html, body { width: 1200px; height: 600px; overflow: hidden; background: var(--paper); }
  .sign {
    position: relative;
    width: 1200px;
    height: 600px;
    overflow: hidden;
    background: var(--paper);
    font-family: "Archivo Black", "Arial Black", sans-serif;
  }
  .sign__shapes { position: absolute; inset: 0; }
  .building-banner {
    position: absolute;
    left: 0; top: 0;
    width: 150px; height: 600px;
    background: linear-gradient(180deg, #b7d2ea 0%, #e6eff8 35%, #f3f7fb 70%, #e9f0f7 100%);
    opacity: 0.85;
  }
  .gallery {
    position: absolute;
    top: 169px;
    left: 132px;
    display: flex;
    gap: 21px;
  }
  .gallery__photo {
    height: 269px;
    border: 1px solid var(--photo-border);
  }
  .gallery__photo--hoist { width: 220px; background: linear-gradient(160deg, #f4f5f7, #c9ced6 60%, #8a7a5a); }
  .gallery__photo--roof { width: 230px; background: linear-gradient(180deg, #a9c9e8 0%, #b34c3e 40%, #e8e2d6 62%, #6f9d45 100%); }
  .gallery__photo--conveyor { width: 229px; background: linear-gradient(170deg, #b38a5a 0%, #d8d0c4 45%, #a48a6c 100%); }
  .gallery__photo--lift { width: 228px; background: linear-gradient(175deg, #e6e3df 0%, #b0453c 35%, #3b63a8 70%, #c9c4bd 100%); }
  .brand {
    position: absolute;
    top: 24px;
    right: 26px;
    display: flex;
    align-items: center;
    gap: 12px;
    color: var(--brand-blue);
  }
  .brand__square { width: 22px; height: 22px; background: var(--brand-blue); }
  .brand__name {
    font-size: 27px;
    line-height: 1.05;
    text-transform: uppercase;
    letter-spacing: 0.5px;
  }
  .address {
    position: absolute;
    left: 30px;
    top: 515px;
    font-size: 39px;
    color: var(--ink);
  }
  .contact {
    position: absolute;
    right: 24px;
    top: 510px;
    text-align: right;
    color: var(--paper);
    font-size: 31px;
    line-height: 1.2;
    letter-spacing: 1px;
  }
</style>
</head>
<body>
  <main class="sign">
    <div class="building-banner" role="img" aria-label="Faded photo of a multi-storey building with a hoist on its facade"></div>

    <svg class="sign__shapes" width="1200" height="600" viewBox="0 0 1200 600" aria-hidden="true">
      <defs>
        <linearGradient id="topBandFill" x1="0" y1="0" x2="1" y2="0">
          <stop offset="0" stop-color="#7fb2dd" stop-opacity="0.55"/>
          <stop offset="0.5" stop-color="#3277b5"/>
          <stop offset="1" stop-color="#1e8fd6"/>
        </linearGradient>
      </defs>
      <polygon points="0,0 640,0 0,190" fill="url(#topBandFill)"/>
      <polygon points="540,600 1200,600 1200,400" fill="#b9d6ee"/>
      <polygon points="575,600 1200,600 1200,418" fill="#1e8fd6"/>
    </svg>

    <div class="brand">
      <span class="brand__square"></span>
      <span class="brand__name">Peak &amp; Rise<br>Hoisting</span>
    </div>

    <div class="gallery">
      <div class="gallery__photo gallery__photo--hoist" role="img" aria-label="Worker on scaffolding beside an electric material hoist"></div>
      <div class="gallery__photo gallery__photo--roof" role="img" aria-label="Ladder hoist lifting solar panels onto a tiled roof"></div>
      <div class="gallery__photo gallery__photo--conveyor" role="img" aria-label="Worker with a belt conveyor moving rubble on a demolition site"></div>
      <div class="gallery__photo gallery__photo--lift" role="img" aria-label="Blue construction lift mounted on building scaffolding"></div>
    </div>

    <p class="address">54 Carrow Street</p>

    <div class="contact">
      <p class="contact__phone">(02) 9418 3065</p>
      <p class="contact__web">www.pk-r.com.au</p>
    </div>
  </main>
</body>
</html>
```